We need a web design for a retail food business based in Greater Western Sydney Australia called Golden Lantern Noodle Restaurant. Basically just need a simple yet easily to navigate website to browse through a menu, gallery , brief description about us, opening hours.
Menu and Gallery will be constantly updated.
Will provide own images for gallery
Updates
Menu has been uploaded and some idea on the colours I would like on the site
Some additional pictures added to see what designs you guys can come up with . Thanks again
To All Designers,
Any extra fee on top of the designs that feels need to be charged, please let me know in advance
Reason: Extending Deadline as I have yet to find a design that I would like...Thanks guys
Target Market(s)
All groups
Industry/Entity Type
Business
Requirements
Must have
- Open minded to any designs
Nice to have
- Would like slideshow behind main logo.
Preferred light coloured site yet not too playful
Should not have
- Preferably no dark colours backgrounds

```html
<!DOCTYPE html>
<html lang="en">
<head>
<meta charset="utf-8">
<title>Golden Lantern Noodle Restaurant – Menu</title>
<link href="https://fonts.googleapis.com/css2?family=Arimo:wght@400;700&display=swap" rel="stylesheet">
<style>
  :root {
    --red: #e8141c;
    --ink: #111111;
    --grey: #7d7d7d;
    --rule: #e6e6e6;
    --paper: #ffffff;
    --photo-a: #f6b24a;
    --photo-b: #e0662e;
    --photo-c: #9a3a1c;
    --art-a: #f7c6dc;
    --art-b: #f3a86a;
    --art-c: #fbe7a8;
  }
  * { box-sizing: border-box; margin: 0; padding: 0; }
  html, body { width: 1200px; height: 1200px; overflow: hidden; background: var(--paper); }
  body { position: relative; font-family: "Arimo", Arial, sans-serif; color: var(--ink); }

  .phone { position: absolute; left: 105px; top: 20px; font-size: 19px; font-weight: 700; letter-spacing: 0.2px; }
  .main-nav { position: absolute; right: 73px; top: 20px; display: flex; gap: 32px; }
  .main-nav a { font-size: 20px; font-weight: 700; color: var(--grey); text-decoration: none; }
  .main-nav a.is-active { color: var(--red); }

  .top-rule { position: absolute; left: 73px; top: 60px; width: 1054px; height: 5px; background: var(--red); }

  .hero-photo {
    position: absolute; left: 73px; top: 65px; width: 1054px; height: 235px;
    background: linear-gradient(100deg, var(--photo-a) 0%, var(--photo-a) 35%, var(--photo-b) 65%, var(--photo-c) 100%);
  }
  .hero-art {
    position: absolute; left: 12px; top: 72px; width: 610px; height: 280px;
    border-radius: 140px 180px 160px 120px / 120px 140px 140px 160px;
    background: radial-gradient(ellipse at 45% 45%, var(--art-c) 0%, var(--art-a) 45%, var(--art-b) 80%, rgba(243,168,106,0) 100%);
  }
  .brand {
    position: absolute; left: 190px; top: 160px; width: 270px;
    font-size: 27px; line-height: 31px; font-weight: 700; color: var(--red);
  }

  .tagline { position: absolute; left: 102px; top: 341px; font-size: 21px; font-weight: 700; letter-spacing: 0.3px; }
  .section-rule { position: absolute; left: 73px; top: 385px; width: 1054px; height: 4px; background: var(--rule); }

  .category-nav { position: absolute; left: 101px; top: 413px; list-style: none; }
  .category-nav li { font-size: 16.5px; line-height: 25.8px; font-weight: 700; color: var(--grey); }
  .category-nav li.is-active { color: var(--red); }

  .menu-column { position: absolute; top: 411px; width: 340px; list-style: none; }
  .menu-column--left { left: 388px; counter-reset: dish 0; }
  .menu-column--right { left: 769px; counter-reset: dish 6; }
  .dish { position: relative; margin-bottom: 19.5px; counter-increment: dish; font-size: 14px; line-height: 20px; }
  .dish::before {
    content: counter(dish) "."; position: absolute; right: 100%; margin-right: 8px;
    color: var(--red); font-weight: 700; font-size: 13.5px;
  }
  .dish-name, .dish-price { color: var(--red); font-weight: 700; font-size: 14px; display: block; }
  .dish-desc { color: var(--ink); width: 328px; }
  .dish--inline-price .dish-name { display: flex; width: 305px; justify-content: space-between; }
</style>
</head>
<body>
  <div class="phone">PHONE (02) 5550 1284</div>
  <nav class="main-nav">
    <a class="is-active" href="#menu">MENU</a>
    <a href="#hours">OPENING HOURS</a>
    <a href="#gallery">GALLERY</a>
    <a href="#about">ABOUT US</a>
    <a href="#contact">CONTACT US</a>
  </nav>

  <div class="top-rule"></div>
  <div class="hero-photo" role="img" aria-label="Slideshow photo of stir-fried crab in golden butter sauce with vertical Chinese calligraphy"></div>
  <div class="hero-art" role="img" aria-label="Illustration of a Chinese dragon among pink and yellow clouds"></div>
  <div class="brand">Golden Lantern Noodle Restaurant</div>

  <h1 class="tagline">LICENCED CHINESE RESTAURANT</h1>
  <div class="section-rule"></div>

  <ul class="category-nav">
    <li class="is-active">Specialty of the house</li>
    <li>Soup</li>
    <li>Entree</li>
    <li>Chicken</li>
    <li>Beef</li>
    <li>Prawns</li>
    <li>Scallops</li>
    <li>Squid</li>
    <li>Pork</li>
    <li>Fillet Steak</li>
    <li>Omlette</li>
    <li>Sweet and Sour</li>
    <li>Lamb</li>
    <li>Fish</li>
    <li>Vegetables</li>
    <li>Duck</li>
    <li>Rice</li>
    <li>Chow Mein (crispy noodle)</li>
    <li>Combination</li>
    <li>Australian Meals</li>
    <li>Desserts</li>
  </ul>

  <ol class="menu-column menu-column--left">
    <li class="dish"><span class="dish-name">SAN CHOY BOW</span><span class="dish-price">14.80</span>
      <p class="dish-desc">A mixture of&nbsp; finely minced pork,water chester nuts,mushrooms And bamboo shoots cooked with a touch of garlic and served With selected lettuce leaves.</p></li>
    <li class="dish"><span class="dish-name">BLACK PEPPER DICED STEAK</span><span class="dish-price">16.80</span>
      <p class="dish-desc">Juciy fillet steak, diced, marinated and cooked in black pepper Sauce, served in a sizzling hot plate.</p></li>
    <li class="dish"><span class="dish-name">CRISPY BEEF PEKING STYLE</span><span class="dish-price">15.50</span>
      <p class="dish-desc">Shredded fillet steak, lightly rolled with corn flour and deep fried, dressed with a light sweet chilli and spicy sauce.</p></li>
    <li class="dish"><span class="dish-name">HONEY KING PRAWNS</span><span class="dish-price">17.80</span>
      <p class="dish-desc">Selected king prawns ,deep fried lightly and stir fried with original honey, served with sesame seed on top.</p></li>
    <li class="dish"><span class="dish-name">MONGOLIAN LAMB</span><span class="dish-price">16.80</span>
      <p class="dish-desc">Finely sliced lamb fillets ,marinated and cooked in a traditional Mongolian sauce and served on a sizzling hot plate.</p></li>
    <li class="dish"><span class="dish-name">SHUN TUNG CHICKEN</span><span class="dish-price">15.20</span>
      <p class="dish-desc">Whole crispy skin chicken deep fried until golden brown and served with a touch of garlic ,chilli and vinegar sauce</p></li>
  </ol>

  <ol class="menu-column menu-column--right">
    <li class="dish"><span class="dish-name">SEAFOOD SUPREME</span><span class="dish-price">22.80</span>
      <p class="dish-desc">A mixture of king prawns,scallops,calamari,fish ,sauced in a rich cream butter sauce.</p></li>
    <li class="dish"><span class="dish-name">GINGER NOODLE</span><span class="dish-price">21.80</span>
      <p class="dish-desc">Selected king prawns marinated and deep fried lightly until crispy and stir fried with five spice salt and fresh chilli.</p></li>
    <li class="dish"><span class="dish-name">FIVE SPICY KING PRAWN</span><span class="dish-price">&nbsp;21.80</span>
      <p class="dish-desc">Selected king prawns marinated and deep fried lightly until crispy and stir fried with five spice salt and fresh chilli.</p></li>
    <li class="dish dish--inline-price"><span class="dish-name"><span>ORANGE HONEY RIBS</span><span>15.80</span></span>
      <p class="dish-desc">Tender short ribs marinated and cooked with honey soya sauce.</p></li>
  </ol>
</body>
</html>
```